"Lanterns Along Every Quiet Road" Sermon Series Design

Needing a design for our church's next sermon series titled "Lanterns Along Every Quiet Road" where we will discuss the need for unity, diversity, love and clarity. Looking for a 1920 x 1080 (or higher res) editable and layered file (PSD or AI) so that we can reformat the design to work on social, screens, lower thirds and various print and online mediums. We will also need to have access to the font files so that we can make resize and tweak as needed. We like the idea of using a globe or map of the world as the backdrop with the words overtop. Or, the idea of creating a bunch of newspaper clippings (generic, so that they can't actually be read) and making the shape of a heart. See attached examples. This website will give you an idea of our previous sermon series designs so you can have an idea of our style (but, feel free to help us advance the ball on something more aligned with current design trends): https://www.brambleford.example/series

Examples use red, but stay away from a ton of red. If you're gonna major in a color, use blue or something in that family.

Must haves:
Title: Lanterns Along Every Quiet Road
Tagline : (TBD - use some Lorem Ipsum as a placeholder and we will fill in later)
Our Logo (attached) (small towards bottom is standard - only use solid colors for logo - preferably just solid black or white)

Industry/Entity Type

Church

Font styles to use
Serif
Sans Serif

Requirements
Must have
• Title: Lanterns Along Every Quiet Road
Nice to have
• We like the idea of using a globe or map of the world as the backdrop with the words overtop. Or, the idea of creating a bunch of newspaper clippings (generic, so that they can't actually be read) and making the shape of a heart. See attached examples.

If you're gonna major on a color, stick with blue or something close.
Should not have
• Don't use red as the primary color (example we sent has red, but stay away from it)

```html
<!DOCTYPE html>
<html lang="en">
<head>
<meta charset="utf-8">
<title>Lanterns Along Every Quiet Road — Sermon Series</title>
<link rel="stylesheet" href="https://fonts.googleapis.com/css2?family=Jost:ital,wght@1,500;1,800&family=Jost:wght@600&display=swap">
<style>
  :root {
    --navy-deep: #1d2f5c;
    --navy-mid: #2c4a85;
    --navy-band: #3a5e9e;
    --globe-light: #c9d3e6;
    --globe-mid: #7f93bd;
    --globe-warm: #b39a9a;
    --paper: #eef1f6;
    --paper-shade: #d9dfea;
    --ink: #1f2b57;
    --ink-soft: #4a5d98;
    --white: #ffffff;
  }
  html, body { margin: 0; padding: 0; overflow: hidden; }
  body { width: 1200px; height: 675px; background: var(--navy-mid); }
  .series-canvas {
    position: relative; width: 1200px; height: 675px; overflow: hidden;
    font-family: "Jost", sans-serif;
  }
  .newsprint-backdrop {
    position: absolute; inset: 0;
    background:
      linear-gradient(176deg, transparent 0 62%, var(--navy-band) 62.4% 100%),
      radial-gradient(ellipse at 40% 60%, #36568f 0%, var(--navy-deep) 100%);
  }
  .globe {
    position: absolute; left: 65px; top: -685px; width: 1120px; height: 1120px;
    border-radius: 50%;
    background:
      radial-gradient(circle at 85% 78%, var(--globe-warm) 0%, transparent 28%),
      radial-gradient(circle at 45% 70%, var(--globe-light) 0%, var(--globe-mid) 55%, #4e6499 100%);
    opacity: 0.92;
  }
  .poster-sheet {
    position: absolute; left: 263px; top: 148px; width: 673px; height: 363px;
    background: linear-gradient(170deg, var(--paper) 0%, #e4e9f2 60%, var(--paper-shade) 100%);
    opacity: 0.94;
    transform: rotate(-0.3deg);
  }
  .series-title {
    position: absolute; left: 263px; top: 196px; width: 673px; margin: 0;
    text-align: center; text-transform: uppercase;
    font-style: italic; font-weight: 800; font-size: 66px;
    line-height: 0.98; letter-spacing: -2px; color: var(--ink);
  }
  .series-tagline {
    position: absolute; left: 263px; top: 420px; width: 673px; margin: 0;
    text-align: center; text-transform: uppercase;
    font-style: italic; font-weight: 500; font-size: 28px;
    letter-spacing: 1px; color: var(--ink-soft);
  }
  .church-signoff {
    position: absolute; left: 0; right: 0; top: 566px;
    display: flex; justify-content: center; align-items: center; gap: 10px;
    color: var(--white); font-weight: 600; font-size: 16px;
    letter-spacing: 3px; text-transform: uppercase;
  }
  .church-signoff .dot {
    width: 22px; height: 22px; border: 2px solid var(--white); border-radius: 50%;
  }
</style>
</head>
<body>
  <main class="series-canvas">
    <div class="newsprint-backdrop" role="img" aria-label="Blue-tinted close-up of printed scripture pages in the background"></div>
    <div class="globe" role="img" aria-label="Photograph of planet Earth from space, seen from above"></div>
    <div class="poster-sheet" role="img" aria-label="Crinkled translucent paper poster pasted over the scene"></div>
    <h1 class="series-title">Lanterns<br>Along Every<br>Quiet Road</h1>
    <p class="series-tagline">Lorem ipsum dolor sit</p>
    <div class="church-signoff"><span class="dot"></span><span>Brambleford Church</span></div>
  </main>
</body>
</html>
```